Muffintop Studio print Advertisement

We are a new online-based store searching for an awesome print advertisement design to use in all our current and future ads. We need an ad that pops and to prompt readers to visit my website (and make a purchase).

Somewhere on the ad, I would like a small section where I can easily change out coupon codes so I can easily differentiate where our marketing effort succeed.

If you think there are any photos on our website that is better suited for the ad, please let us know and we'll post it up here for you to use!

Ad size should be 2.1875"width (656px) x 2.8"height (840px).

www.muffintopstudio-example.com

Target Market(s)

Female age 16 to 40.

Requirements
Must have
• Section where we can put coupon code.

```html
<!DOCTYPE html>
<html lang="en">
<head>
<meta charset="utf-8">
<title>Muffintop Studio – Print Advertisement</title>
<link rel="stylesheet" href="https://fonts.googleapis.com/css2?family=Fredoka:wght@400;500;600&family=Nunito:wght@700;800&display=swap">
<style>
  :root{
    --page:#efeae6;
    --sky:#c4e6f7;
    --sky-deep:#8fcdee;
    --panel:#fde7ea;
    --panel-edge:#ffffff;
    --rose:#ee8495;
    --rose-soft:#f7b8c3;
    --rose-text:#e26b80;
    --white:#ffffff;
  }
  *{margin:0;padding:0;box-sizing:border-box}
  html,body{width:1200px;height:900px;overflow:hidden;background:var(--page)}
  .ad{
    position:absolute;left:272px;top:30px;width:656px;height:840px;
    background:var(--sky);overflow:hidden;
    box-shadow:0 6px 18px rgba(0,0,0,.12);
  }
  .panel{
    position:absolute;left:20px;top:50px;width:616px;height:770px;
    background:var(--panel);border:4px solid var(--panel-edge);border-radius:26px;
  }
  .url-bar{
    position:absolute;left:236px;top:54px;width:396px;height:42px;
    background:var(--sky-deep);border-radius:0 22px 0 22px;
    display:flex;align-items:center;justify-content:center;
    font-family:"Nunito",sans-serif;font-weight:800;font-size:18px;color:var(--white);
    letter-spacing:.3px;white-space:nowrap;
  }
  .brand{
    position:absolute;left:30px;top:58px;width:196px;height:90px;
    display:flex;align-items:center;justify-content:center;gap:10px;
  }
  .brand-dot{width:20px;height:20px;border-radius:50%;background:var(--rose);flex:none}
  .brand-name{
    font-family:"Fredoka",sans-serif;font-weight:600;font-size:28px;line-height:1.02;
    color:var(--rose-text);
  }
  .coupon{
    position:absolute;left:10px;top:170px;width:172px;height:112px;
    border:3px solid var(--rose-soft);border-radius:10px;overflow:hidden;background:var(--white);
  }
  .coupon-head{height:48px;display:flex;align-items:center;gap:8px;padding:0 10px}
  .coupon-brand{font-family:"Fredoka",sans-serif;font-weight:600;font-size:12px;line-height:1;color:var(--rose-text);width:56px}
  .coupon-tag{
    background:var(--rose);color:var(--white);font-family:"Fredoka",sans-serif;
    font-size:17px;padding:2px 10px;border-radius:4px;
  }
  .coupon-value{
    height:58px;background:var(--sky-deep);color:var(--white);
    font-family:"Nunito",sans-serif;font-weight:800;font-size:32px;
    display:flex;align-items:center;padding-left:16px;
  }
  .category{position:absolute;width:148px;margin-left:-74px;text-align:center}
  .ring{
    width:116px;height:116px;margin:0 auto;border-radius:50%;
    background:var(--rose);padding:8px;
  }
  .ring .photo{
    width:100px;height:100px;border-radius:50%;border:5px solid var(--white);
    background:radial-gradient(circle at 40% 35%,#fff6f2,#e8c8b8 70%,#c99a86);
  }
  .label{
    margin-top:4px;font-family:"Fredoka",sans-serif;font-weight:500;font-size:18px;
    line-height:1.05;color:var(--rose-text);white-space:nowrap;
  }
  .c1{left:103px}.c2{left:253px}.c3{left:403px}.c4{left:553px}
  .r1{top:132px}.r2{top:292px}.r3{top:454px}.r4{top:616px}
</style>
</head>
<body>
<main class="ad">
  <div class="panel"></div>
  <div class="url-bar">www.muffintopstudio-example.com</div>

  <header class="brand">
    <span class="brand-dot"></span>
    <span class="brand-name">Muffintop<br>Studio</span>
  </header>

  <section class="coupon">
    <div class="coupon-head">
      <span class="coupon-brand">Muffintop Studio</span>
      <span class="coupon-tag">coupon</span>
    </div>
    <div class="coupon-value">15% off</div>
  </section>

  <div class="category c2 r1"><div class="ring"><div class="photo" role="img" aria-label="Product photo: bags"></div></div><p class="label">bags</p></div>
  <div class="category c3 r1"><div class="ring"><div class="photo" role="img" aria-label="Product photo: beauty"></div></div><p class="label">beauty</p></div>
  <div class="category c4 r1"><div class="ring"><div class="photo" role="img" aria-label="Product photo: bracelet"></div></div><p class="label">bracelet</p></div>

  <div class="category c1 r2"><div class="ring"><div class="photo" role="img" aria-label="Product photo: other beauty"></div></div><p class="label">other beauty</p></div>
  <div class="category c2 r2"><div class="ring"><div class="photo" role="img" aria-label="Product photo: earrings"></div></div><p class="label">earrings</p></div>
  <div class="category c3 r2"><div class="ring"><div class="photo" role="img" aria-label="Product photo: paper goods"></div></div><p class="label">paper goods</p></div>
  <div class="category c4 r2"><div class="ring"><div class="photo" role="img" aria-label="Product photo: new arrivals"></div></div><p class="label">new</p></div>

  <div class="category c1 r3"><div class="ring"><div class="photo" role="img" aria-label="Product photo: necklaces"></div></div><p class="label">necklaces</p></div>
  <div class="category c2 r3"><div class="ring"><div class="photo" role="img" aria-label="Product photo: rubber stamps"></div></div><p class="label">rubber stamps</p></div>
  <div class="category c3 r3"><div class="ring"><div class="photo" role="img" aria-label="Product photo: stationery"></div></div><p class="label">stationery</p></div>
  <div class="category c4 r3"><div class="ring"><div class="photo" role="img" aria-label="Product photo: best sellers"></div></div><p class="label">best sellers</p></div>

  <div class="category c1 r4"><div class="ring"><div class="photo" role="img" aria-label="Product photo: stickers and sticky pads"></div></div><p class="label">sticker &amp;<br>sticky pads</p></div>
  <div class="category c2 r4"><div class="ring"><div class="photo" role="img" aria-label="Product photo: pens, pencils and cases"></div></div><p class="label">pens, pencils<br>&amp; cases</p></div>
  <div class="category c3 r4"><div class="ring"><div class="photo" role="img" aria-label="Product photo: phone accessories"></div></div><p class="label">phone<br>accessories</p></div>
  <div class="category c4 r4"><div class="ring"><div class="photo" role="img" aria-label="Product photo: other stationery"></div></div><p class="label">other<br>stationary</p></div>
</main>
</body>
</html>
```